serious, thorough, light and simple - that's my advice and mediations

My business card should combine my logo (uploaded file) and my homepage (https://fellor-mediation.webnestsite.com).

Contact Information for Business Card

Name: Sabine Fellor di Vanti
Phone: 076 412 58 94
mail: sfellor@postkiv.ch
web: www.fellor-di-vanti.ch

```html
<!DOCTYPE html>
<html lang="de">
<head>
<meta charset="utf-8">
<title>Sabine Fellor di Vanti – Visitenkarte</title>
<link href="https://fonts.googleapis.com/css2?family=Mulish:wght@400;500;600&family=Oswald:wght@500&display=swap" rel="stylesheet">
<style>
  :root {
    --stage: #e4e5e5;
    --gold: #a08450;
    --paper: #f4f4f4;
    --white: #ffffff;
    --green: #2e6b4a;
    --navy: #2c3e6b;
    --ink: #333333;
  }
  * { margin: 0; padding: 0; box-sizing: border-box; }
  html, body { width: 1200px; height: 960px; overflow: hidden; }
  body {
    background: var(--stage);
    font-family: "Mulish", sans-serif;
    position: relative;
  }
  .card {
    position: absolute;
    left: 336px;
    width: 527px;
    height: 341px;
  }
  .card--front { top: 123px; background: var(--gold); color: var(--white); }
  .card--back  { top: 494px; background: var(--paper); }

  .brand {
    position: absolute;
    left: 0; right: 0;
    display: flex;
    justify-content: center;
  }
  .card--front .brand { top: 142px; }
  .card--back .brand { top: 92px; }

  .brand__name {
    display: flex;
    align-items: center;
    gap: 12px;
    font-family: "Mulish", sans-serif;
    font-weight: 500;
    font-size: 40px;
    letter-spacing: 1px;
    line-height: 1;
  }
  .brand__dot {
    width: 16px; height: 16px;
    border-radius: 50%;
    background: currentColor;
  }
  .card--back .brand__name { color: var(--gold); font-size: 36px; }

  .brand__glow {
    position: absolute;
    left: 130px;
    width: 260px;
    height: 22px;
    border-radius: 50%;
  }
  .card--front .brand__glow { top: 268px; background: radial-gradient(closest-side, rgba(60,45,20,.28), rgba(60,45,20,0)); }
  .card--back .brand__glow { top: 186px; left: 165px; width: 200px; height: 18px; background: radial-gradient(closest-side, rgba(0,0,0,.12), rgba(0,0,0,0)); }

  .holder {
    position: absolute;
    left: 79px;
    top: 255px;
    font-family: "Oswald", sans-serif;
    font-weight: 500;
    font-size: 18px;
    color: var(--gold);
    text-transform: uppercase;
  }
  .divider {
    position: absolute;
    left: 263px;
    top: 237px;
    width: 2px;
    height: 59px;
    background: var(--green);
  }
  .contacts {
    position: absolute;
    left: 281px;
    top: 238px;
    list-style: none;
    font-size: 14px;
    color: var(--ink);
  }
  .contacts li {
    display: flex;
    align-items: center;
    gap: 5px;
    height: 18.5px;
  }
  .contacts svg { width: 12px; height: 12px; fill: none; stroke: var(--navy); }
</style>
</head>
<body>

<section class="card card--front" aria-label="Vorderseite">
  <div class="brand">
    <div class="brand__name"><span class="brand__dot"></span>Wege im Dialog</div>
  </div>
  <div class="brand__glow"></div>
</section>

<section class="card card--back" aria-label="Rückseite">
  <div class="brand">
    <div class="brand__name"><span class="brand__dot"></span>Wege im Dialog</div>
  </div>
  <div class="brand__glow"></div>

  <div class="holder">Sabine Fellor di Vanti</div>
  <div class="divider"></div>
  <ul class="contacts">
    <li>
      <svg viewBox="0 0 12 12"><path d="M2.5 1h2l1 3-1.3.9a6 6 0 0 0 2.9 2.9L8 6.5l3 1v2A1.5 1.5 0 0 1 9.5 11 8.5 8.5 0 0 1 1 2.5 1.5 1.5 0 0 1 2.5 1z" fill="var(--navy)" stroke="none"/></svg>
      076 412 58 94
    </li>
    <li>
      <svg viewBox="0 0 12 12" stroke-width="1.3"><rect x="1" y="2.5" width="10" height="7"/><path d="M1 2.5l5 4 5-4"/></svg>
      sfellor@postkiv.ch
    </li>
    <li>
      <svg viewBox="0 0 12 12" stroke-width="1"><circle cx="6" cy="6" r="5"/><ellipse cx="6" cy="6" rx="2.2" ry="5"/><path d="M1 6h10M2 3.5h8M2 8.5h8"/></svg>
      www.fellor-di-vanti.ch
    </li>
  </ul>
</section>

</body>
</html>
```